Business Consultancy Business Card Design

Business Card design required for Business Analysis and Project Consultancy business based in Scotland.

Company Name - Brevick Advisory

Back - Company Logo

Front Details

Owen Brevick
07642 918 305
owen.brevick@brevickadvisory.com
http://www.brevickadvisory.com

Colours should match the logo colours but I am open to design ideas.

```html
<!DOCTYPE html>
<html lang="en">
<head>
<meta charset="utf-8">
<title>Brevick Advisory – Business Card</title>
<link href="https://fonts.googleapis.com/css2?family=Questrial&family=Open+Sans:wght@400;700&display=swap" rel="stylesheet">
<style>
  :root {
    --backdrop: #e9eaec;
    --card-blue: #1fa3dd;
    --card-rim: #6f7173;
    --panel-light: #f4f4f5;
    --panel-mid: #d6d7d9;
    --panel-dark: #b9babc;
    --ink: #2b2b2d;
    --ink-soft: #3f4042;
    --mark: #1fa3dd;
  }
  * { margin: 0; padding: 0; box-sizing: border-box; }
  html, body {
    width: 1200px; height: 902px; overflow: hidden;
    background: var(--backdrop);
  }
  .stage {
    width: 1200px; height: 902px;
    display: flex; align-items: center; justify-content: center;
  }
  .card {
    width: 980px; height: 620px;
    border-radius: 300px / 290px;
    background: var(--card-blue);
    padding: 26px;
    box-shadow: 0 14px 30px rgba(0,0,0,0.12);
  }
  .card-rim {
    width: 100%; height: 100%;
    border-radius: 280px / 270px;
    background: var(--card-rim);
    padding: 7px;
  }
  .card-face {
    position: relative;
    width: 100%; height: 100%;
    border-radius: 274px / 264px;
    background: radial-gradient(ellipse at 52% 45%, var(--panel-light) 0%, var(--panel-mid) 65%, var(--panel-dark) 100%);
    font-family: "Open Sans", sans-serif;
    color: var(--ink);
  }
  .brand {
    position: absolute; top: 118px; left: 150px;
    display: flex; align-items: center; gap: 22px;
  }
  .brand-dot {
    width: 58px; height: 58px; border-radius: 50%;
    background: var(--mark);
  }
  .brand-name {
    font-family: "Questrial", sans-serif;
    font-size: 48px; letter-spacing: 1px;
    color: var(--ink-soft);
    text-transform: uppercase;
  }
  .person {
    position: absolute; top: 275px; left: 300px;
  }
  .person-name {
    font-weight: 700; font-size: 34px; letter-spacing: 0.5px;
    text-transform: uppercase;
  }
  .person-role {
    font-size: 22px; margin-left: 40px; margin-top: -4px;
  }
  .contact {
    position: absolute; top: 410px; right: 120px;
    text-align: right; font-size: 19px; line-height: 30px;
    color: var(--ink);
  }
  .contact-line { display: flex; align-items: center; justify-content: flex-end; gap: 8px; }
  .contact-line svg { width: 14px; height: 16px; fill: var(--ink); }
</style>
</head>
<body>
<main class="stage">
  <article class="card">
    <div class="card-rim">
      <div class="card-face">
        <div class="brand">
          <span class="brand-dot"></span>
          <span class="brand-name">Brevick Advisory</span>
        </div>
        <div class="person">
          <p class="person-name">Owen Brevick</p>
          <p class="person-role">Managing Director</p>
        </div>
        <div class="contact">
          <p class="contact-line">owen.brevick@brevickadvisory.com</p>
          <p class="contact-line">
            <svg viewBox="0 0 14 18" aria-hidden="true"><path d="M7 0C3.1 0 0 3.1 0 7c0 5 7 11 7 11s7-6 7-11c0-3.9-3.1-7-7-7zm0 9.5A2.5 2.5 0 1 1 7 4.5a2.5 2.5 0 0 1 0 5z"/></svg>
            12 Harbour Row, Leith, Edinburgh EH6
          </p>
          <p class="contact-line">
            <svg viewBox="0 0 14 18" aria-hidden="true"><path d="M3 1l3 3-1.5 2.5c1 2 2.5 3.5 4.5 4.5L11.5 9.5l3 3-2 3C7 14 1.5 8 0.5 3z"/></svg>
            07642 918 305 &nbsp;@ www.brevickadvisory.com
          </p>
        </div>
      </div>
    </div>
  </article>
</main>
</body>
</html>
```